Luxury skin care/beauty salon needs a fresh wordpress website makeover

Today we have a wordpress site that has served us well, and we want to stay with wordpress, but we need a new up to date fresh look, with an inviting and enticing front, and look that just draws people in to book an appoint for luxury beauty treatment.

The salon consists of beautisian/skin specialint, a cosmetical nurse, and a doctor, - so top notch expertice within skin care and beauty treatment.

- The site should be integrated with Postwren (which we currently do not use.

- The site should further be able to "show prices for treatments" in a manner that matches the new website in style and layout, - we do show prices today via ex. the booking module from a vendor, but its done via iFrame

- booking needs to be very easy and intuitive, and the site needs to be response, since 75% of our customers use Ipad or mobile phone while booking

- the colours of the logo and style for the company today is primarily gold and black, and the shop is kept in a minimalistic style

- we have fresh newly made professional pictures made, and we can also later supply a video for ex. a landing page

- we have a license for Framewick if that can be utilized

- we need to be able to translate all elements into minimum Norwegian

- we use QL and Snapvale today to promote our services, if that can be incorporated, that would be a promotion plus

today we have the following pages
- main page
- a treatment page, where treatments are in more detail explained, this also doubles as pricelist ... we might look to discard this, since its manually updated and is not the master ... the master is the booking system, which also contains princes
- a portfolio page, seperated into types of treatments, this page also has one element of Snapvale which is one of the prime social media channals.
- a team member page, that presents the staff
- a contact us page
- a booking page ( that uses the national available booking system that we want to keep, but present in a different manner if possible) .. including gift card

we are not nessesarily looking to keep all pages, if the new design comes up with a more proffesional and smoother look, so this is debatable, so i have left the "How many web pages do you need designed?" to 4 pages .. again debatable

The final design should communicate luxury and professional skincare and beauty treatments, and easy booking.

Target Market(s)

Women or men that want to book a beauty or skin care treatment

Industry/Entity Type

Beauty and skin care salon

Coding

Coded - Design and coding required

Number of Pages Required

4 page

Colors

Designer to choose colors to be used in the design.

Requirements
Must have
• booking system, a connection to postwren, ability to change wording/language (Norwegian)
Nice to have
• video background, if it compliments the design
Should not have
• a new booking platform, we want to stick with the one we have

```html
<!DOCTYPE html>
<html lang="en">
<head>
<meta charset="utf-8">
<title>Aurum – Beauty Salon</title>
<link href="https://fonts.googleapis.com/css2?family=Montserrat:wght@200;300;400;500&display=swap" rel="stylesheet">
<style>
:root{
  --gold:#b8975a;
  --gold-soft:#c4ab7c;
  --gold-line:#dcc9a3;
  --cream:#fbe9c6;
  --ink:#1d1d1d;
  --text:#6f6a62;
  --black:#000;
  --white:#fff;
}
*{margin:0;padding:0;box-sizing:border-box}
html,body{width:1200px;height:3534px;overflow:hidden}
body{position:relative;background:var(--white);font-family:"Montserrat",sans-serif;color:var(--ink)}
.abs{position:absolute}
.glow{position:absolute;border-radius:50%;background:radial-gradient(circle,rgba(214,196,160,.55) 0%,rgba(214,196,160,0) 70%)}
.photo{position:absolute}

/* header */
.site-header{position:absolute;left:0;top:0;width:1200px;height:60px;background:var(--black)}
.brand{position:absolute;left:158px;top:8px;font-size:38px;font-weight:400;letter-spacing:2px;color:var(--gold)}
.main-nav a{position:absolute;top:23px;font-size:13px;color:var(--gold);text-decoration:none;letter-spacing:.3px}
.menu-toggle{position:absolute;left:1024px;top:24px;width:18px}
.menu-toggle span{display:block;height:2px;background:var(--gold);margin-bottom:4px}

/* buttons */
.btn{position:absolute;border:1.5px solid var(--gold);background:var(--white);font-size:14px;color:var(--ink);display:flex;align-items:center;justify-content:center;letter-spacing:.3px}
.btn-line{position:absolute;height:1px;background:var(--gold)}

/* hero */
.hero-kicker{left:291px;top:217px;font-size:21px;font-weight:400;letter-spacing:.5px}
.hero-title{left:140px;width:367px;text-align:right;top:250px;font-size:104px;line-height:1.1;font-weight:200;color:var(--gold);letter-spacing:-3px;white-space:nowrap}
.hero-ghost{left:474px;top:380px;font-size:78px;font-weight:700;line-height:.95;color:transparent;-webkit-text-stroke:1px #eee}

/* about */
.section-title{font-size:40px;font-weight:200;color:#333}
.section-title em{font-style:normal;color:var(--gold)}
.about-text{left:583px;width:440px;font-size:14px;line-height:19px;color:var(--text);font-weight:300}

/* treatments */
.treat-sub{left:157px;top:1562px;font-size:18px;color:var(--gold);font-weight:300}
.price-row{position:absolute;height:30px;border-bottom:1px solid #e3e3e3;font-size:13px}
.price-row .name{position:absolute;left:13px;top:2px}
.price-row .dash{position:absolute;left:0;top:10px;width:7px;height:1px;background:#999}
.price-row .amount{position:absolute;right:0;top:12px}
.ghost-vertical{left:1080px;top:1371px;writing-mode:vertical-rl;font-size:70px;font-weight:600;color:transparent;-webkit-text-stroke:1px #e4e4e4;letter-spacing:3px}

/* portfolio */
.portfolio-band{left:0;top:1998px;width:1200px;height:131px;background:var(--gold-soft)}
.portfolio-ghost{left:52px;top:2025px;font-size:84px;font-weight:700;color:rgba(255,255,255,.07);letter-spacing:2px}
.portfolio-title{left:0;width:1200px;top:2042px;text-align:center;font-size:40px;font-weight:300;color:var(--white)}
.thumb{position:absolute;width:205px;height:205px;border:1px solid var(--gold-line);background:var(--white)}
.thumb .photo{left:11px;top:11px;width:181px;height:181px}
.tab{position:absolute;left:668px;width:301px;height:56px;border:1.5px solid var(--gold-line);font-size:19px;color:var(--gold-soft);padding-left:16px;display:flex;align-items:center;font-weight:400}
.tab.active{background:var(--gold-soft);color:var(--white);border-color:var(--gold-soft)}

/* contact */
.contact-card{left:522px;top:2856px;width:499px;height:518px;background:var(--gold-soft)}
.contact-card .inner{position:absolute;left:19px;top:19px;right:19px;bottom:19px;border:1px solid rgba(255,255,255,.45)}
.contact-title{left:580px;top:2898px;font-size:40px;font-weight:200;color:var(--white)}
.field-label{left:590px;font-size:11px;color:var(--white)}
.field-line{left:587px;width:353px;height:1px;background:rgba(255,255,255,.6)}
.partner{top:3282px;font-size:20px;font-weight:500;color:var(--ink);letter-spacing:1px}

/* footer */
.site-footer{left:0;top:3443px;width:1200px;height:91px;background:var(--black)}
.footer-copy{left:158px;top:3482px;font-size:12px;color:#bbb}
.footer-follow{left:913px;top:3482px;font-size:12px;color:#bbb}
.footer-follow b{font-weight:400;color:var(--gold)}
</style>
</head>
<body>

<div class="glow" style="left:-250px;top:270px;width:520px;height:520px"></div>
<div class="glow" style="left:980px;top:60px;width:400px;height:400px"></div>
<div class="glow" style="left:900px;top:1060px;width:520px;height:520px"></div>
<div class="glow" style="left:-200px;top:2320px;width:420px;height:420px"></div>

<header class="site-header">
  <div class="brand">AURUM</div>
  <nav class="main-nav">
    <a style="left:463px">HOME</a>
    <a style="left:546px">TREATMENT</a>
    <a style="left:662px">PORTFOLIO</a>
    <a style="left:777px">TEAM MEMBER</a>
    <a style="left:915px">CONTACT US</a>
  </nav>
  <div class="menu-toggle"><span></span><span></span><span></span></div>
</header>

<!-- hero -->
<section class="hero">
  <div class="abs" style="left:0;top:227px;width:281px;height:1px;background:var(--gold)"></div>
  <div class="abs" style="left:0;top:232px;width:281px;height:1px;background:var(--gold-line)"></div>
  <div class="abs hero-kicker">WELCOME TO AURUM</div>
  <div class="abs hero-title">AURUM</div>
  <div class="abs hero-ghost">BEAUTY<br>SALON</div>
  <div class="btn" style="left:197px;top:399px;width:124px;height:40px">BOOK NOW</div>
  <div class="btn-line" style="left:321px;top:419px;width:63px"></div>

  <svg class="abs" style="left:700px;top:110px" width="420" height="320" viewBox="0 0 420 320">
    <ellipse cx="210" cy="160" rx="185" ry="100" transform="rotate(28 210 160)" fill="none" stroke="#d7bb84" stroke-width="1.5"/>
  </svg>
  <div class="photo" role="img" aria-label="Portrait of a woman with long curly brown hair" style="left:684px;top:167px;width:355px;height:340px;border-radius:178px 178px 0 0;background:linear-gradient(160deg,var(--cream) 0%,#c99a72 45%,#6a4330 100%)"></div>

  <svg class="abs" style="left:615px;top:248px" width="120" height="120" viewBox="0 0 120 120">
    <defs><path id="ring" d="M60,60 m-46,0 a46,46 0 1,1 92,0 a46,46 0 1,1 -92,0"/></defs>
    <text font-family="Montserrat, sans-serif" font-size="10" letter-spacing="3" fill="#333">
      <textPath href="#ring" startOffset="0%">Beauty salon in central</textPath>
    </text>
    <path d="M57,54 L65,60 L57,66 Z" fill="#111"/>
  </svg>

  <svg class="abs" style="left:574px;top:562px" width="50" height="50" viewBox="0 0 50 50">
    <circle cx="25" cy="25" r="24" fill="none" stroke="#eee"/>
    <rect x="19.5" y="15" width="11" height="19" rx="5.5" fill="none" stroke="#b8975a" stroke-width="1.3"/>
    <line x1="25" y1="19" x2="25" y2="23" stroke="#b8975a" stroke-width="1.3"/>
  </svg>
</section>

<!-- about -->
<section class="about">
  <div class="photo" role="img" aria-label="Woman with smooth skin touching her cheek" style="left:159px;top:695px;width:394px;height:315px;background:linear-gradient(120deg,#f2f2f2 0%,#e9d5c3 50%,#d9b59c 100%)"></div>
  <div class="photo" role="img" aria-label="Woman with bob haircut, video preview" style="left:229px;top:1010px;width:388px;height:314px;background:linear-gradient(135deg,#8d7f93 0%,#d8c3b8 55%,#efe6e4 100%)"></div>
  <div class="abs" style="left:273px;top:1045px;width:264px;height:245px;background:rgba(196,171,124,.55)"></div>
  <svg class="abs" style="left:389px;top:1145px" width="52" height="52" viewBox="0 0 52 52">
    <circle cx="26" cy="26" r="24" fill="none" stroke="#fff" stroke-width="2"/>
    <path d="M21,17 L35,26 L21,35 Z" fill="#fff"/>
  </svg>
  <div class="photo" role="img" aria-label="Close-up of pink lips and blonde hair" style="left:521px;top:940px;width:387px;height:277px;background:linear-gradient(120deg,#efe6e2 0%,#e4b8b8 45%,#ddd2cb 100%)"></div>

  <h2 class="abs section-title" style="left:580px;top:690px">Welcome to <em>AURUM</em></h2>
  <div class="abs" style="left:583px;top:750px;width:78px;height:1px;background:var(--gold)"></div>
  <p class="abs about-text" style="top:768px">Beauty salon in central Solvik. We focus on high competence, exceptional service and the feeling of luxury in everyday life.</p>
  <p class="abs about-text" style="top:845px">The salon was established in the beginning of 2021 by Mira and Sofie Lind. These two amazing ladies are passionate about the industry.</p>
</section>

<!-- treatments -->
<section class="treatments">
  <div class="abs" style="left:159px;top:1400px;width:1px;height:81px;background:var(--gold-line)"></div>
  <div class="abs" style="left:0;top:1451px;width:853px;height:1px;background:var(--gold-line)"></div>
  <div class="abs" style="left:853px;top:1451px;width:1px;height:50px;background:var(--gold-line)"></div>
  <div class="abs" style="left:0;top:1881px;width:686px;height:1px;background:var(--gold-line)"></div>
  <div class="abs ghost-vertical">TREATMENTS</div>

  <h2 class="abs section-title" style="left:155px;top:1506px">Treatments</h2>
  <div class="abs treat-sub">10% student and military discount on all treatments</div>

  <div class="price-row" style="left:159px;top:1603px;width:229px"><span class="name">FACIAL</span><span class="amount">$50</span></div>
  <div class="price-row" style="left:159px;top:1639px;width:229px"><span class="dash"></span><span class="name">MEDICAL SKIN CARE</span><span class="amount">$50</span></div>
  <div class="price-row" style="left:159px;top:1675px;width:229px"><span class="dash"></span><span class="name">INJECTIONS</span><span class="amount">$50</span></div>
  <div class="price-row" style="left:159px;top:1711px;width:229px"><span class="dash"></span><span class="name">HAIR REMOVAL</span><span class="amount">$50</span></div>
  <div class="price-row" style="left:159px;top:1747px;width:229px"><span class="dash"></span><span class="name">BRYN</span><span class="amount">$50</span></div>

  <div class="price-row" style="left:452px;top:1603px;width:203px"><span class="name">LASHES</span><span class="amount">$50</span></div>
  <div class="price-row" style="left:452px;top:1639px;width:203px"><span class="dash"></span><span class="name">NAILS</span><span class="amount">$50</span></div>
  <div class="price-row" style="left:452px;top:1675px;width:203px"><span class="dash"></span><span class="name">MICROBLADING</span><span class="amount">$50</span></div>
  <div class="price-row" style="left:452px;top:1711px;width:203px"><span class="dash"></span><span class="name">PACKAGES</span><span class="amount">$50</span></div>
  <div class="price-row" style="left:452px;top:1747px;width:203px"><span class="dash"></span><span class="name">MAKEUP</span><span class="amount">$50</span></div>

  <div class="btn" style="left:158px;top:1807px;width:123px;height:40px">BOOK TIME</div>
  <div class="btn-line" style="left:281px;top:1827px;width:62px;background:var(--gold-line)"></div>

  <div class="photo" role="img" aria-label="Portrait of a woman with voluminous curly hair" style="left:686px;top:1505px;width:353px;height:408px;border-radius:177px 177px 0 0;background:linear-gradient(150deg,#9aa09a 0%,#8a6656 45%,#d9b49b 100%)"></div>
</section>

<!-- portfolio -->
<section class="portfolio">
  <div class="abs" style="left:585px;top:1971px;width:1px;height:53px;background:var(--gold-line)"></div>
  <div class="abs portfolio-band"></div>
  <div class="abs portfolio-ghost">PORTFOLIO</div>
  <h2 class="abs portfolio-title">Portfolio</h2>

  <div class="abs" style="left:230px;top:2193px;width:1px;height:540px;background:#eee3cf"></div>
  <div class="abs" style="left:230px;top:2733px;width:970px;height:1px;background:#eee3cf"></div>
  <div class="abs" style="left:590px;top:2232px;width:610px;height:1px;background:#eee3cf"></div>

  <div class="thumb" style="left:160px;top:2188px"><div class="photo" role="img" aria-label="Eyebrow before and after treatment" style="background:linear-gradient(90deg,#a9a49a 0%,#c9b2a0 50%,#d9b4a8 100%)"></div></div>
  <div class="thumb" style="left:385px;top:2255px"><div class="photo" role="img" aria-label="Hands with nude manicure" style="background:linear-gradient(135deg,#5a5e60 0%,#c9a596 55%,#555a5c 100%)"></div></div>
  <div class="thumb" style="left:160px;top:2416px"><div class="photo" role="img" aria-label="Hands with nude manicure" style="background:linear-gradient(135deg,#5a5e60 0%,#c9a596 55%,#555a5c 100%)"></div></div>
  <div class="thumb" style="left:378px;top:2483px"><div class="photo" role="img" aria-label="Hands with nude manicure" style="background:linear-gradient(135deg,#5a5e60 0%,#c9a596 55%,#555a5c 100%)"></div></div>

  <div class="tab active" style="top:2265px">Vippeextensions</div>
  <div class="abs" style="left:969px;top:2292px;width:28px;height:1px;background:var(--gold-line)"></div>
  <div class="tab" style="top:2331px">Rocker lift</div>
  <div class="tab" style="top:2397px">Nails</div>
  <div class="tab" style="top:2462px">Bryn</div>
  <div class="tab" style="top:2528px">@Lashes by Mira</div>

  <div class="btn" style="left:675px;top:2643px;width:123px;height:39px">READ MORE</div>
  <div class="btn-line" style="left:798px;top:2662px;width:63px;background:var(--gold-line)"></div>
</section>

<!-- contact -->
<section class="contact">
  <div class="photo" role="img" aria-label="Smiling beautician with glasses standing in the salon" style="left:0;top:2813px;width:624px;height:438px;background:linear-gradient(100deg,#6b5a4c 0%,#e4d3c2 35%,#b0866a 65%,#3a302a 100%)"></div>
  <div class="abs partner" style="left:158px">Veluna</div>
  <div class="abs partner" style="left:314px;letter-spacing:3px">AURELLE</div>

  <div class="abs contact-card"><div class="inner"></div></div>
  <h2 class="abs contact-title">Contact Us</h2>
  <div class="abs field-label" style="top:2984px">Name *</div>
  <div class="abs field-line" style="top:3007px"></div>
  <div class="abs field-label" style="top:3050px">Email *</div>
  <div class="abs field-line" style="top:3071px"></div>
  <div class="abs field-label" style="top:3116px">Phone *</div>
  <div class="abs field-line" style="top:3137px"></div>
  <div class="abs field-label" style="top:3206px">Message *</div>
  <div class="abs field-line" style="top:3245px"></div>
  <div class="btn" style="left:591px;top:3286px;width:123px;height:39px;background:transparent;border-color:var(--white);color:var(--white)">READ MORE</div>
  <div class="btn-line" style="left:714px;top:3305px;width:63px;background:rgba(255,255,255,.7)"></div>
</section>

<footer class="abs site-footer"></footer>
<div class="abs footer-copy">© All rights reserved - Aurum Salong AS</div>
<div class="abs footer-follow">FOLLOW US &nbsp;<b>QL</b> &nbsp;<b>Snapvale</b></div>

</body>
</html>
```